Business Card Design needed for logo design project

Our company needs a Business Card Design. Please refer to our original project in the link above.
Dorian Whitlock
Broker

W: Grandvistaestates.com
P: 214-555-0187
F: 267-555-0142
E: dorianwhitlock@ferncrestmail.com
A: North Dallas Office

Name Spelling update , sorry Dorian Whitlock card is double sided

```html
<!DOCTYPE html>
<html lang="en">
<head>
<meta charset="utf-8">
<title>Grand Vista Estates – Business Card</title>
<link rel="stylesheet" href="https://fonts.googleapis.com/css2?family=Crimson+Pro:ital,wght@0,400;0,600;0,700;1,400&display=swap">
<style>
  :root {
    --stage-light: #e4e4e4;
    --stage-dark: #8d8d8d;
    --card-black: #050505;
    --brand-gold: #c9a56e;
    --green-light: #8edcaa;
    --green-mid: #2fbe66;
    --green-deep: #14ac52;
    --ink: #0c1a10;
    --card-shadow: rgba(0, 0, 0, 0.35);
  }

  * { box-sizing: border-box; margin: 0; padding: 0; }

  html, body {
    width: 1200px;
    height: 900px;
    overflow: hidden;
  }

  body {
    background: radial-gradient(ellipse at 50% 60%, var(--stage-light) 0%, #cfcfcf 45%, var(--stage-dark) 100%);
    font-family: "Crimson Pro", "Times New Roman", serif;
    position: relative;
  }

  .business-card {
    position: absolute;
    left: 180px;
    top: 210px;
    width: 840px;
    height: 480px;
    display: flex;
    box-shadow: 0 18px 40px var(--card-shadow);
  }

  .card-brand-side {
    width: 480px;
    height: 100%;
    background: var(--card-black);
    display: flex;
    flex-direction: column;
    align-items: center;
    padding-top: 120px;
  }

  .brand-mark {
    display: flex;
    flex-direction: column;
    align-items: center;
    gap: 22px;
  }

  .brand-dot {
    width: 64px;
    height: 64px;
    border-radius: 50%;
    background: var(--brand-gold);
  }

  .brand-name {
    color: var(--brand-gold);
    font-weight: 600;
    font-size: 30px;
    letter-spacing: 2px;
    text-transform: uppercase;
  }

  .contact-email {
    margin-top: 64px;
    color: var(--brand-gold);
    font-size: 25px;
    letter-spacing: 0.3px;
  }

  .card-contact-side {
    width: 360px;
    height: 100%;
    background: radial-gradient(circle at 48% 52%, var(--green-light) 0%, var(--green-mid) 48%, var(--green-deep) 100%);
    position: relative;
    padding: 42px 0 0 30px;
    color: var(--ink);
  }

  .agent-name {
    font-weight: 700;
    font-size: 34px;
    letter-spacing: 0.6px;
    line-height: 1.1;
  }

  .agent-title {
    font-style: italic;
    font-size: 28px;
    line-height: 1.1;
    margin-top: 2px;
  }

  .faint-emblem {
    position: absolute;
    left: 120px;
    top: 160px;
    width: 120px;
    height: 120px;
    border-radius: 50%;
    background: rgba(255, 255, 255, 0.14);
  }

  .phone-list {
    position: absolute;
    left: 90px;
    top: 330px;
    list-style: none;
    font-size: 25px;
    line-height: 1.3;
  }

  .website {
    position: absolute;
    left: 26px;
    bottom: 20px;
    font-size: 27px;
    letter-spacing: 0.3px;
  }
</style>
</head>
<body>
  <article class="business-card">
    <section class="card-brand-side">
      <div class="brand-mark">
        <span class="brand-dot"></span>
        <span class="brand-name">Grand Vista Estates</span>
      </div>
      <p class="contact-email">dorianwhitlock@ferncrestmail.com</p>
    </section>

    <section class="card-contact-side">
      <h1 class="agent-name">Dorian Whitlock</h1>
      <p class="agent-title">Broker</p>
      <span class="faint-emblem" aria-hidden="true"></span>
      <ul class="phone-list">
        <li>214-555-0187</li>
        <li>267-555-0142</li>
      </ul>
      <p class="website">Grandvistaestates.com</p>
    </section>
  </article>
</body>
</html>
```